Werbeplakat für Frisörsalon
Zielgruppe
Frisörsalon (Coiffeursalon Lindenhof) mit hohem Qualitätsstandard im mittel-hohem Preissegment. Zielgruppe hauptsächlich Frauen (20j - 40j). Jedoch bieten wir auch Herrenfrisuren an.
Aufgabenstellung
Format --> A1
auf erstem Blick erkennbar das es sich um einen Frisörsalon handelt
Text:
erstklassige Damen- und Herrenfrisuren
moderne Kinderfrisuren
Waschen, Schneiden, Föhnen
Färben, Tönung, Mèches
VERANTIQ Behandlung
Hochstecken / Hochzeitsfrisuren / Gala
Warme Farben
Logo auf dem Plakat in Originalfarben
Dame auf dem Plakat mit langem lockigem dichtem Haar (Rotschopf)

```html
<!DOCTYPE html>
<html lang="de">
<head>
<meta charset="utf-8">
<title>Coiffeursalon Lindenhof – Plakat</title>
<link rel="stylesheet" href="https://fonts.googleapis.com/css2?family=Playfair+Display:wght@800&family=Lato:wght@400&display=swap">
<style>
  :root {
    --page-bg: #ffffff;
    --hair-dark: #5a2c18;
    --hair-mid: #a2542c;
    --hair-light: #c9834f;
    --skin: #d9a98a;
    --backdrop: #2c3f45;
    --frame-white: #ffffff;
    --brand-red: #8e1a1e;
    --text-white: #ffffff;
  }
  * { margin: 0; padding: 0; box-sizing: border-box; }
  html, body {
    width: 1200px; height: 2730px; overflow: hidden;
    background: var(--page-bg);
  }
  .poster {
    position: absolute; left: 40px; top: 571px;
    width: 1120px; height: 1587px; overflow: hidden;
    box-shadow: 0 12px 28px rgba(0,0,0,0.35);
  }
  .poster-photo {
    position: absolute; inset: 0;
    background:
      radial-gradient(ellipse 34% 44% at 56% 44%, var(--skin) 0%, rgba(217,169,138,0.85) 55%, rgba(217,169,138,0) 100%),
      radial-gradient(ellipse 30% 18% at 55% 80%, rgba(205,150,118,0.9) 0%, rgba(205,150,118,0) 100%),
      radial-gradient(ellipse 70% 60% at 50% 50%, var(--hair-light) 0%, var(--hair-mid) 55%, var(--hair-dark) 100%),
      linear-gradient(180deg, var(--backdrop) 0%, var(--hair-dark) 40%);
  }
  .poster-frame {
    position: absolute; left: 27px; top: 43px;
    width: 1067px; height: 1503px;
    border: 8px solid var(--frame-white);
  }
  .headline {
    position: absolute; left: 60px; right: 60px; top: 134px;
    text-align: center; color: var(--text-white);
    font-family: "Playfair Display", serif; font-weight: 800;
    font-size: 40px; line-height: 50px; letter-spacing: 0.2em;
    padding-left: 0.2em;
    text-shadow: 0 1px 3px rgba(0,0,0,0.25);
  }
  .brand-name {
    position: absolute; left: 0; right: 0; top: 935px;
    text-align: center; color: var(--brand-red);
    font-family: "Lato", sans-serif; font-weight: 400;
    font-size: 40px; letter-spacing: 0.06em;
  }
  .rule {
    position: absolute; left: 186px; width: 746px; height: 7px;
    background: var(--frame-white);
  }
  .rule--top { top: 1050px; }
  .rule--bottom { top: 1388px; }
  .services {
    position: absolute; left: 0; right: 0; top: 1076px;
    list-style: none; text-align: center; color: var(--text-white);
    font-family: "Lato", sans-serif; font-weight: 400;
    font-size: 40px; line-height: 58px; text-transform: uppercase;
  }
  .services .service--small { font-size: 29px; line-height: 62px; }
  .contact {
    position: absolute; left: 0; right: 0; top: 1450px;
    text-align: center; color: var(--text-white);
    font-family: "Lato", sans-serif; font-weight: 400; font-size: 28px;
  }
  .contact .divider { margin: 0 16px; }
</style>
</head>
<body>
  <main class="poster">
    <div class="poster-photo" role="img" aria-label="Porträtfoto einer Frau mit langem, lockigem rotem Haar vor dunklem Hintergrund"></div>
    <div class="poster-frame"></div>
    <h1 class="headline">ERSTKLASSIGE<br>DAMEN- UND HERRENFRISUREN</h1>
    <p class="brand-name">Coiffeursalon Lindenhof</p>
    <div class="rule rule--top"></div>
    <ul class="services">
      <li>Moderne Kinderfrisuren</li>
      <li>Waschen, Schneiden, Föhnen</li>
      <li>Färben, Tönung, Mèches</li>
      <li>VERANTIQ Behandlung</li>
      <li class="service--small">Hochstecken / Hochzeitsfrisuren / Gala</li>
    </ul>
    <div class="rule rule--bottom"></div>
    <p class="contact">Marktgasse 18, 4500 Solothurn<span class="divider">|</span>T: 032 555 01 47</p>
  </main>
</body>
</html>
```